Corvane Lending Partners. Professional and Established Company

A full service finance company specializing in obtaining capital for small business. Business Lending advisor, helping small business owners access the capital they need to launch, grow, or sustain their business. Many of our programs offer flexible guidelines to overcome common obstacles such as credit score, credit history, and time in business, financials, and industry type. Our streamlined funding process makes getting a business loan, business line of credit, stated income commercial real estate loan, a smooth and stress free experience.SOME OF THE MOST COMMON NEEDS FOR BUSINESS CAPITAL:• Working Capital• Debt Consolidations (loans, merchant cash advances, etc.)• Payroll• Operating Expenses• Inventory• Equipment Financing• Commercial Real Estate (Purchase, Fix & Flip, Rehab, Renovations)• Business Acquisitions• Business ExpansionWe like the websites:www.brookfellcap.com they are in the same industry and provide the same servicesWe are wanting to be able to update when we do press releases and such using Word Press. Our look should be very professional and we will be adding Our Team Professional Bios and Headshots.

Industry/Entity Type

Finance

Number of Pages Required

5+ page

Font styles to use
Serif
Sans Serif

Requirements
Must have
• We want to copy brookfellcap.com
• We need:
• Home Page
• About Us
• Loan Programs
• Loan Criteria
• News
• Apply Now
• Contact
Nice to have
• See brookfellcap.com
Should not have
• Need professional design. Nothing bright or abstract

```html
<!DOCTYPE html>
<html lang="en">
<head>
<meta charset="utf-8">
<title>Corvane Lending Partners</title>
<link href="https://fonts.googleapis.com/css2?family=Montserrat:ital,wght@0,400;0,500;0,600;0,700;0,800;1,400&display=swap" rel="stylesheet">
<style>
:root{
  --blue:#2f78bd;
  --blue-dark:#1f5f9f;
  --hero:#4c93cf;
  --hero-deep:#3f86c6;
  --ink:#3a3a3a;
  --light:#f4f5f7;
  --footer:#2a2a2c;
  --white:#ffffff;
}
*{margin:0;padding:0;box-sizing:border-box}
html,body{width:1200px;height:2626px;overflow:hidden}
body{font-family:"Montserrat",sans-serif;color:var(--ink);background:var(--white);position:relative}

/* header */
.site-header{position:absolute;left:0;top:0;width:1200px;height:80px;background:var(--white)}
.brand{position:absolute;left:137px;top:18px;font-size:15px;font-weight:700;color:var(--blue);line-height:18px;display:flex;align-items:center;gap:8px}
.brand .mark{width:14px;height:14px;background:var(--blue);flex:none}
.top-contact{position:absolute;top:16px;font-size:11.5px;color:#777;display:flex;align-items:center;gap:7px;white-space:nowrap}
.top-contact svg{width:11px;height:11px;fill:var(--blue)}
.apply-btn{position:absolute;left:946px;top:8px;width:118px;height:28px;background:var(--blue);color:#fff;font-size:11px;font-weight:700;display:flex;align-items:center;justify-content:center}
.main-nav{position:absolute;top:50px;right:136px;display:flex;gap:17px;font-size:11.5px;font-weight:500;color:#444}

/* hero */
.hero{position:absolute;left:0;top:80px;width:1200px;height:497px;background:linear-gradient(120deg,var(--hero-deep) 0%,var(--hero) 50%,#6aaee0 100%)}
.hero-title{position:absolute;left:0;top:125px;width:1200px;text-align:center;color:#fff;font-size:46px;font-weight:800;line-height:53px}
.hero-lede{position:absolute;left:300px;top:243px;width:600px;text-align:center;color:#fff;font-size:11.5px;line-height:21px}
.hero-arrow{position:absolute;top:218px;width:14px;height:22px;stroke:#fff;stroke-width:1.5;fill:none}
.deal{position:absolute;top:357px;width:150px;text-align:center;color:#fff}
.deal .kind{font-size:10px;font-weight:700;letter-spacing:2.5px}
.deal .amount{font-size:15px;font-weight:700;letter-spacing:1px;margin-top:5px}
.deal .place{font-size:10px;font-style:italic;line-height:18px;margin-top:4px}
.deal.faded{opacity:.55}
.deal-divider{position:absolute;top:358px;width:1px;height:88px;background:rgba(255,255,255,.55)}
.deal-track{position:absolute;left:152px;top:467px;width:895px;height:2px;background:var(--blue-dark)}
.deal-active{position:absolute;left:553px;top:467px;width:102px;height:2px;background:#fff}

/* section titles */
.section-title{position:absolute;left:0;width:1200px;text-align:center}
.section-title h2{display:inline-block;font-size:19px;font-weight:700;color:#3a3a3a;padding:0 22px 4px;border-bottom:2px solid var(--blue)}

/* loan grid */
.loan-tile{position:absolute;width:296px;height:150px}
.loan-tile .photo{position:absolute;inset:0}
.loan-tile .label{position:absolute;left:0;bottom:0;width:100%;height:32px;background:rgba(0,0,0,.45);color:#fff;font-size:13px;font-weight:700;padding:8px 12px}
.land-card{position:absolute;inset:8px;background:rgba(0,0,0,.55);color:#fff;text-align:center}
.land-card h3{font-size:13px;font-weight:700;margin-top:32px}
.land-card p{font-size:11.5px;line-height:19px;margin:12px 36px 0}
.outline-btn{position:absolute;left:454px;top:1247px;width:298px;height:43px;border:1px solid var(--blue);color:var(--blue);font-size:11px;font-weight:700;display:flex;align-items:center;justify-content:center}

/* advisor band */
.band-rule{position:absolute;left:0;top:1331px;width:1200px;height:7px;background:#e6ebf1}
.advisor{position:absolute;left:0;top:1338px;width:1200px;height:377px;background:var(--blue)}
.advisor h2{position:absolute;left:136px;top:54px;width:420px;color:#fff;font-size:19px;font-weight:700;line-height:30px}
.advisor p{position:absolute;left:136px;width:420px;color:#e3eefa;font-size:11px;line-height:19.5px}
.white-btn{position:absolute;left:137px;top:270px;width:139px;height:40px;background:#fff;color:var(--blue);font-size:11px;font-weight:700;display:flex;align-items:center;justify-content:center}
.video{position:absolute;left:623px;top:44px;width:445px;height:281px;background:linear-gradient(135deg,#4a4641,#2e2b28 60%,#3b3834)}
.play{position:absolute;left:202px;top:112px;width:56px;height:56px;border-radius:50%;background:var(--blue);display:flex;align-items:center;justify-content:center}

/* blog */
.blog-bg{position:absolute;left:0;top:1715px;width:1200px;height:587px;background:var(--light)}
.post{position:absolute;top:1854px;width:296px;height:366px;background:#fff;box-shadow:0 2px 6px rgba(0,0,0,.12)}
.post .photo{height:194px}
.post h3{font-size:16px;font-weight:500;color:#333;margin:24px 0 0 23px}
.post p{font-size:11px;line-height:19.5px;color:#777;margin:13px 20px 0 26px}
.post .meta{position:absolute;left:26px;right:16px;bottom:16px;display:flex;justify-content:space-between;font-size:11px;color:#888}
.post .meta span{display:flex;align-items:center;gap:7px}
.post .meta svg{width:12px;height:12px;fill:var(--blue)}

/* footer */
.site-footer{position:absolute;left:0;top:2302px;width:1200px;height:324px;background:var(--footer);color:#ddd}
.footer-brand{position:absolute;left:138px;top:86px;width:190px;font-size:15px;font-weight:700;line-height:20px;color:#5d9bd6;display:flex;align-items:center;gap:8px}
.footer-brand .mark{width:12px;height:12px;background:#5d9bd6;flex:none}
.footer-col h4{position:absolute;top:79px;font-size:11px;font-weight:700;color:#fff;letter-spacing:.5px}
.contact-row{position:absolute;left:348px;font-size:12px;display:flex;gap:16px;align-items:center}
.contact-row svg{width:13px;height:13px;fill:#fff}
.useful-links{position:absolute;left:625px;top:112px;list-style:none;font-size:11px;line-height:24px}
.socials{position:absolute;left:836px;top:110px;display:flex;gap:17px}
.socials span{width:24px;height:22px}
.copyright{position:absolute;left:0;top:297px;width:1200px;text-align:center;font-size:9px;color:#555}
</style>
</head>
<body>

<header class="site-header">
  <div class="brand"><span class="mark"></span><span>Corvane Lending<br>Partners</span></div>
  <div class="top-contact" style="left:674px">
    <svg viewBox="0 0 24 24"><path d="M6.6 10.8a15 15 0 0 0 6.6 6.6l2.2-2.2c.3-.3.7-.4 1-.2 1.1.4 2.3.6 3.6.6.6 0 1 .4 1 1V20c0 .6-.4 1-1 1A17 17 0 0 1 3 4c0-.6.4-1 1-1h3.5c.6 0 1 .4 1 1 0 1.3.2 2.5.6 3.6.1.3 0 .7-.2 1z"/></svg>01632 960 214</div>
  <div class="top-contact" style="left:797px">
    <svg viewBox="0 0 24 24"><path d="M2 5h20v3l-10 6L2 8zM2 10l10 6 10-6v9H2z"/></svg>info@corvane.com</div>
  <div class="apply-btn">APPLY NOW</div>
  <nav class="main-nav">
    <span>ABOUT US</span><span>LOAN PROGRAMS</span><span>LOAN CLOSINGS</span><span>LOAN CRITERIA</span><span>NEWS</span><span>CONTACT US</span>
  </nav>
</header>

<section class="hero" role="img" aria-label="Blue-toned photo of hands working at a keyboard">
  <svg class="hero-arrow" style="left:100px" viewBox="0 0 14 22"><path d="M11 2 2 11l9 9"/></svg>
  <svg class="hero-arrow" style="left:1083px" viewBox="0 0 14 22"><path d="M3 2l9 9-9 9"/></svg>
  <h1 class="hero-title">FULL SERVICE<br>FINANCE COMPANY</h1>
  <p class="hero-lede">Business Lending advisor, helping small business owners access the capital they need to launch, grow, or sustain their business. Many of our programs offer flexible guidelines to overcome.</p>

  <div class="deal" style="left:144px"><div class="kind">MIXED-USE</div><div class="amount">$15,000,000</div><div class="place">TOWNHOUSE<br>MANHATTAN, NY</div></div>
  <div class="deal-divider" style="left:308px"></div>
  <div class="deal" style="left:336px"><div class="kind">MIXED-USE</div><div class="amount">$15,000,000</div><div class="place">TOWNHOUSE<br>MANHATTAN, NY</div></div>
  <div class="deal-divider" style="left:508px"></div>
  <div class="deal" style="left:531px"><div class="kind">MIXED-USE</div><div class="amount">$15,000,000</div><div class="place">TOWNHOUSE<br>MANHATTAN, NY</div></div>
  <div class="deal-divider" style="left:708px"></div>
  <div class="deal faded" style="left:723px"><div class="kind">MIXED-USE</div><div class="amount">$15,000,000</div><div class="place">TOWNHOUSE<br>MANHATTAN, NY</div></div>
  <div class="deal-divider" style="left:908px"></div>
  <div class="deal faded" style="left:926px"><div class="kind">MIXED-USE</div><div class="amount">$15,000,000</div><div class="place">TOWNHOUSE<br>MANHATTAN, NY</div></div>
  <div class="deal-track"></div>
  <div class="deal-active"></div>
</section>

<div class="section-title" style="top:628px"><h2>LOAN PROGRAMS</h2></div>

<div class="loan-tile" style="left:134px;top:695px">
  <div class="photo" role="img" aria-label="Photo of open green land" style="background:linear-gradient(160deg,#3e5a38,#2a4a2a 60%,#4a6b3a)"></div>
  <div class="land-card"><h3>LAND LOAN</h3><p>We are one of a select few private lenders to specialize in land loans...</p></div>
</div>
<div class="loan-tile" style="left:454px;top:695px">
  <div class="photo" role="img" aria-label="Photo of a hotel reception desk" style="background:linear-gradient(135deg,#4a3526,#8a6a4e 55%,#c9a57d)"></div>
  <div class="label">HOSPITALITY LOANS</div></div>
<div class="loan-tile" style="left:772px;top:695px">
  <div class="photo" role="img" aria-label="Photo of an apartment complex with a pool" style="background:linear-gradient(180deg,#d9e2ea,#9a6a62 45%,#4aa8d0)"></div>
  <div class="label">MULTIFAMILY LOANS</div></div>

<div class="loan-tile" style="left:134px;top:877px">
  <div class="photo" role="img" aria-label="Photo of an open-plan office" style="background:linear-gradient(180deg,#c9cccf,#8a8f94 55%,#3f4448)"></div>
  <div class="label">OFFICE LOANS</div></div>
<div class="loan-tile" style="left:454px;top:877px">
  <div class="photo" role="img" aria-label="Photo of a lit tower building at dusk" style="background:linear-gradient(160deg,#1d2a5e,#3a4fa0 55%,#2a3370)"></div>
  <div class="label">MIXED-USE LOANS</div></div>
<div class="loan-tile" style="left:772px;top:877px">
  <div class="photo" role="img" aria-label="Photo of a shopping mall interior" style="background:linear-gradient(180deg,#c8c8c4,#7a6f62 55%,#4a4038)"></div>
  <div class="label">RETAIL LOANS</div></div>

<div class="loan-tile" style="left:134px;top:1058px">
  <div class="photo" role="img" aria-label="Photo of an industrial refinery at dusk" style="background:linear-gradient(180deg,#7d8fb8,#c89a8a 50%,#3d3a40)"></div>
  <div class="label">INDUSTRIAL LOANS</div></div>
<div class="loan-tile" style="left:454px;top:1058px">
  <div class="photo" role="img" aria-label="Photo of warehouse shelving" style="background:linear-gradient(135deg,#3a3028,#8a5a3a 50%,#4a5a78)"></div>
  <div class="label">WAREHOUSE LOANS</div></div>
<div class="loan-tile" style="left:772px;top:1058px">
  <div class="photo" role="img" aria-label="Photo of self storage units with blue doors" style="background:linear-gradient(180deg,#4a8ad0,#dfe3e8 45%,#2a5ea8)"></div>
  <div class="label">SELF STORAGE LOANS</div></div>

<div class="outline-btn">VIEW LOAN PROGRAMS</div>

<div class="band-rule"></div>
<section class="advisor">
  <h2>BEST FINANCIAL ADVISOR FOR YOUR BUSINESS&nbsp; TO GROWUP</h2>
  <p style="top:133px">Parchitect beatae vitae dicta sunt explicabo. Nemo enim ipsam voluptatem quia voluptas sit aspernatur aut odit aut fugit, sed quia consequuntur magni dolores eos qui ratione voluptatem sequi nesciunt.</p>
  <p style="top:210px">Perspiciatis unde omnis iste natus error sit voluptatem accusantium doloremque laudantium, totam rem aperiam, eaque ipsa quae</p>
  <div class="white-btn">READ MORE</div>
  <div class="video" role="img" aria-label="Video still of a team meeting around a table, seen from above">
    <div class="play"><svg width="16" height="18" viewBox="0 0 16 18"><path d="M2 1l13 8-13 8z" fill="#fff"/></svg></div>
  </div>
</section>

<div class="blog-bg"></div>
<div class="section-title" style="top:1787px"><h2>OUR BLOG</h2></div>

<article class="post" style="left:133px">
  <div class="photo" role="img" aria-label="Photo of two students looking at a laptop" style="background:linear-gradient(135deg,#c9d3d8,#9aa4a8 50%,#6a5a52)"></div>
  <h3>Lorem Ipsum is simply</h3>
  <p>Lorem ipsum dolor sit amet, consectetur adipiscing elit, sed do eiusmod tempor incididunt ut labore et dolore magna aliqua.</p>
  <div class="meta"><span><svg viewBox="0 0 24 24"><path d="M12 2a10 10 0 1 0 0 20 10 10 0 0 0 0-20zm0 3a7 7 0 1 1 0 14 7 7 0 0 1 0-14zm-1 2v6l5 3 1-1.6-4-2.4V7z"/></svg>Sep 10’ 15</span><span><svg viewBox="0 0 24 24"><path d="M2 3h14v10H7l-5 4zM18 7h4v13l-4-3H9v-2h9z"/></svg>5 Coments</span></div>
</article>
<article class="post" style="left:453px">
  <div class="photo" role="img" aria-label="Photo of a child with arms outstretched at sunset" style="background:linear-gradient(180deg,#b7a6c9,#e7b08a 55%,#9a5a3a)"></div>
  <h3>Lorem Ipsum is simply</h3>
  <p>Lorem ipsum dolor sit amet, consectetur adipiscing elit, sed do eiusmod tempor incididunt ut labore et dolore magna aliqua.</p>
  <div class="meta"><span><svg viewBox="0 0 24 24"><path d="M12 2a10 10 0 1 0 0 20 10 10 0 0 0 0-20zm0 3a7 7 0 1 1 0 14 7 7 0 0 1 0-14zm-1 2v6l5 3 1-1.6-4-2.4V7z"/></svg>Sep 10’ 15</span><span><svg viewBox="0 0 24 24"><path d="M2 3h14v10H7l-5 4zM18 7h4v13l-4-3H9v-2h9z"/></svg>5 Coments</span></div>
</article>
<article class="post" style="left:773px">
  <div class="photo" role="img" aria-label="Photo of a business team at a desk" style="background:linear-gradient(180deg,#e8ece8,#b8bfb8 55%,#3a3a3f)"></div>
  <h3>Lorem Ipsum is simply</h3>
  <p>Lorem ipsum dolor sit amet, consectetur adipiscing elit, sed do eiusmod tempor incididunt ut labore et dolore magna aliqua.</p>
  <div class="meta"><span><svg viewBox="0 0 24 24"><path d="M12 2a10 10 0 1 0 0 20 10 10 0 0 0 0-20zm0 3a7 7 0 1 1 0 14 7 7 0 0 1 0-14zm-1 2v6l5 3 1-1.6-4-2.4V7z"/></svg>Sep 10’ 15</span><span><svg viewBox="0 0 24 24"><path d="M2 3h14v10H7l-5 4zM18 7h4v13l-4-3H9v-2h9z"/></svg>5 Coments</span></div>
</article>

<footer class="site-footer">
  <div class="footer-brand"><span class="mark"></span><span>Corvane Lending<br>Partners</span></div>
  <div class="footer-col"><h4 style="left:348px">GET IN TOUCH</h4></div>
  <div class="contact-row" style="top:113px"><svg viewBox="0 0 24 24"><path d="M7 1h10v22H7zM9 3v16h6V3z"/></svg>204-555-0187</div>
  <div class="contact-row" style="top:149px;font-size:11.5px"><svg viewBox="0 0 24 24"><path d="M22 2 2 10l9 3 3 9z"/></svg>42 Harlow Terrace</div>
  <div class="contact-row" style="top:178px;left:377px;font-size:11.5px">Ashvale VIC 3190 Australia</div>
  <div class="contact-row" style="top:207px"><svg viewBox="0 0 24 24"><path d="M2 5h20v3l-10 6L2 8zM2 10l10 6 10-6v9H2z"/></svg>hello@corvane.com</div>
  <div class="footer-col"><h4 style="left:625px">USEFUL LINKS</h4></div>
  <ul class="useful-links"><li>About us</li><li>Loan Programs</li><li>Loan Closings</li><li>Loan Criteria</li><li>News</li><li>Contact</li></ul>
  <div class="footer-col"><h4 style="left:836px">FOLLOW US</h4></div>
  <div class="socials">
    <span style="background:#3aa3e0"></span><span style="background:#3b5a9a"></span><span style="background:#d34836"></span><span style="background:#d9302a"></span>
  </div>
  <div class="copyright">Copyright 2018 corvane.com. All rights reserved</div>
</footer>

</body>
</html>
```